Managed Service Provider need new business cards

We are a small Maanged Service Provider of IT Services and need a new fresh design for our business cards. We want something impossible, fun and professional :)
Our services has a large range, but we are always fun and make sure our customers both get their issue sorted and also feel like they are "catching up with an old friend".
All our cards in the past has always been all black, with red and we need something fresher.
The back of card, we would like just a small list of what we do i think, but if someone has a better idea, please do something cool with the back of the card:
Managed IT Services
Productivity Solutions
Data Backup and Recovery
IT System Maintenance
Managed IT Security
More details can be found on our website tqnetworks.com.au
Industry/Entity Type
It Company
Contact Information for Business Card
Name: Dwayne Falstrup
Title: Director
Phone: 03 6193 4827
Mobile: 0412 587 239
Email: dwayne@tqnetworks.com.au
Web: www.tqnetworks.com.au

```html
<!DOCTYPE html>
<html lang="en">
<head>
<meta charset="utf-8">
<title>TQ Networks – Business Cards</title>
<link href="https://fonts.googleapis.com/css2?family=Montserrat:wght@400;500;700;800&display=swap" rel="stylesheet">
<style>
  :root {
    --backdrop: #e4e4e4;
    --card: #222222;
    --red: #e3171f;
    --white: #ffffff;
  }
  * { margin: 0; padding: 0; box-sizing: border-box; }
  html, body {
    width: 1200px; height: 801px; overflow: hidden;
    background: var(--backdrop);
    font-family: "Montserrat", sans-serif;
  }
  .canvas {
    position: relative; width: 1200px; height: 801px;
    display: flex; align-items: center; justify-content: center; gap: 44px;
  }
  .card {
    position: relative;
    width: 520px; height: 318px;
    background: var(--card);
    border-bottom: 3px solid var(--red);
    border-right: 2px solid var(--red);
    color: var(--white);
  }
  .brand {
    display: flex; align-items: center; gap: 12px;
    color: var(--red); font-weight: 800; letter-spacing: 0.5px;
    white-space: nowrap;
  }
  .brand-dot {
    background: var(--red); border-radius: 50%; flex: none;
  }

  /* Front */
  .card-front .brand {
    position: absolute; left: 0; right: 0; top: 62px;
    justify-content: center; font-size: 40px;
  }
  .card-front .brand-dot { width: 18px; height: 18px; }
  .details {
    position: absolute; left: 0; right: 0; top: 168px;
    display: flex; justify-content: center; align-items: stretch; gap: 18px;
  }
  .identity { text-align: right; }
  .identity .name { color: var(--red); font-weight: 700; font-size: 20px; line-height: 1.2; }
  .identity .title { font-size: 14px; font-weight: 500; margin-top: 2px; }
  .identity .web { font-size: 13px; font-weight: 500; margin-top: 10px; }
  .identity .web em { font-style: normal; color: var(--red); }
  .divider { width: 1.5px; background: var(--red); }
  .contacts { list-style: none; display: flex; flex-direction: column; justify-content: center; gap: 7px; }
  .contacts li { display: flex; align-items: center; gap: 8px; font-size: 14px; font-weight: 500; }
  .contacts svg { width: 13px; height: 13px; flex: none; }

  /* Back */
  .card-back .brand {
    position: absolute; left: 0; right: 0; top: 92px;
    justify-content: center; font-size: 50px;
  }
  .card-back .brand-dot { width: 22px; height: 22px; }
  .services {
    position: absolute; left: 30px; right: 30px; top: 208px;
    text-align: center; font-size: 13.5px; font-weight: 500; line-height: 1.7;
  }
  .services .sep { color: var(--red); margin: 0 4px; }
</style>
</head>
<body>
<main class="canvas">

  <section class="card card-front" aria-label="Business card front">
    <div class="brand"><span class="brand-dot"></span>TQ Networks</div>
    <div class="details">
      <div class="identity">
        <p class="name">Dwayne Falstrup</p>
        <p class="title">Director</p>
        <p class="web">www.<em>tqnetworks</em>.com.au</p>
      </div>
      <div class="divider"></div>
      <ul class="contacts">
        <li>
          <svg viewBox="0 0 24 24" aria-hidden="true"><path fill="#e3171f" d="M6.6 10.8a15 15 0 0 0 6.6 6.6l2.2-2.2a1 1 0 0 1 1-.25 11.4 11.4 0 0 0 3.6.57 1 1 0 0 1 1 1V20a1 1 0 0 1-1 1A17 17 0 0 1 3 4a1 1 0 0 1 1-1h3.5a1 1 0 0 1 1 1c0 1.25.2 2.45.57 3.57a1 1 0 0 1-.25 1z"/></svg>
          03 6193 4827
        </li>
        <li>
          <svg viewBox="0 0 24 24" aria-hidden="true"><rect x="6" y="2" width="12" height="20" rx="2" fill="none" stroke="#e3171f" stroke-width="2"/><circle cx="12" cy="18" r="1.2" fill="#e3171f"/></svg>
          0412 587 239
        </li>
        <li>
          <svg viewBox="0 0 24 24" aria-hidden="true"><rect x="2" y="5" width="20" height="14" fill="#e3171f"/><path d="M2 5l10 8 10-8" fill="none" stroke="#222" stroke-width="1.8"/></svg>
          dwayne@tqnetworks.com.au
        </li>
      </ul>
    </div>
  </section>

  <section class="card card-back" aria-label="Business card back">
    <div class="brand"><span class="brand-dot"></span>TQ Networks</div>
    <p class="services">
      Managed IT Services<span class="sep">•</span>Productivity Solutions<span class="sep">•</span>Data Backup and Recovery<br>
      <span class="sep">•</span>IT System Maintenance<span class="sep">•</span>Managed IT Security
    </p>
  </section>

</main>
</body>
</html>
```